biz card for insurance Agent
Insurance Agency Biz card
biz card for insurance Agent - Health
Creative Brief
Professional
Marla Tovesby
Insurance Agent
NC & SC
marlatovesby@quillmail.example
please create a design for the back of the card, and we'll add the text to it later

```html
<!DOCTYPE html>
<html lang="en">
<head>
<meta charset="utf-8">
<title>Marla Tovesby – Business Card</title>
<link rel="stylesheet" href="https://fonts.googleapis.com/css2?family=Roboto:ital,wght@0,400;0,700;0,900;1,400&display=swap">
<style>
  :root {
    --backdrop-light: #8a8a8a;
    --backdrop-dark: #4e4e4e;
    --card-blue: #4f93c8;
    --card-blue-deep: #2f6fa3;
    --accent-red: #c8202a;
    --accent-red-deep: #7e0f15;
    --navy: #13233f;
    --white: #ffffff;
    --map-tint: rgba(255,255,255,.22);
    --map-tint-soft: rgba(255,255,255,.08);
  }
  * { box-sizing: border-box; margin: 0; padding: 0; }
  html, body { width: 1200px; height: 607px; overflow: hidden; }
  body {
    font-family: "Roboto", Arial, sans-serif;
    background: radial-gradient(ellipse at center, var(--backdrop-light) 0%, var(--backdrop-dark) 100%);
    position: relative;
  }
  .card {
    position: absolute;
    top: 149px;
    width: 540px;
    height: 309px;
    overflow: hidden;
    box-shadow: 0 10px 28px rgba(0,0,0,.35);
    background: linear-gradient(160deg, var(--card-blue) 0%, var(--card-blue-deep) 100%);
  }
  .card--front { left: 40px; }
  .card--back { left: 620px; }
  .card-shapes { position: absolute; inset: 0; }

  .map-area {
    position: absolute;
    border-radius: 10px;
    background: linear-gradient(135deg, var(--map-tint), var(--map-tint-soft));
  }
  .card--front .map-area { left: 196px; top: 70px; width: 76px; height: 56px; }
  .card--back .map-area { left: 290px; top: 60px; width: 190px; height: 170px; border-radius: 18px; }

  .brand {
    position: absolute;
    display: flex;
    align-items: center;
    gap: 10px;
  }
  .brand-mark { width: 22px; height: 22px; background: var(--accent-red); flex: none; }
  .brand-name {
    font-weight: 900;
    text-transform: uppercase;
    color: var(--navy);
    line-height: 1;
    letter-spacing: .5px;
  }
  .card--front .brand { left: 28px; top: 36px; }
  .card--front .brand-name { font-size: 22px; }

  .contact {
    position: absolute;
    left: 28px;
    bottom: 36px;
    color: var(--white);
    font-size: 12px;
    line-height: 1.55;
  }
  .contact .region { font-weight: 700; }

  .identity {
    position: absolute;
    right: 28px;
    top: 24px;
    text-align: right;
    color: var(--white);
  }
  .identity-name { font-size: 19px; font-weight: 700; }
  .identity-role { font-size: 13px; font-style: italic; margin-top: 2px; }

  .portrait {
    position: absolute;
    right: 30px;
    bottom: 0;
    width: 170px;
    height: 215px;
    border-radius: 80px 80px 0 0;
    background: linear-gradient(180deg, #5a3a2c 0%, #2a1a16 55%, #121212 100%);
  }

  .card--back .brand { left: 120px; top: 130px; }
  .card--back .brand-mark { width: 40px; height: 40px; background: var(--white); }
  .card--back .brand-name { font-size: 30px; color: var(--white); }
</style>
</head>
<body>

  <section class="card card--front" aria-label="Card front">
    <svg class="card-shapes" viewBox="0 0 540 309" width="540" height="309" aria-hidden="true">
      <defs>
        <linearGradient id="red-panel" x1="0" y1="0" x2="0" y2="1">
          <stop offset="0" stop-color="#c8202a"/>
          <stop offset="1" stop-color="#7e0f15"/>
        </linearGradient>
      </defs>
      <path d="M300 0 H540 V309 H330 C 360 220, 290 90, 300 0 Z" fill="url(#red-panel)"/>
      <path d="M292 0 C 282 90, 352 220, 322 309" fill="none" stroke="#13233f" stroke-width="7"/>
    </svg>

    <div class="map-area" role="img" aria-label="Small map of the service region"></div>

    <div class="brand">
      <span class="brand-mark"></span>
      <span class="brand-name">Tarrow Bay<br>Insurance</span>
    </div>

    <div class="contact">
      <p class="region">NC &amp; SC</p>
      <p class="phone">Tel: 704.555.0148</p>
      <p class="email">email: marlatovesby@quillmail.example</p>
    </div>

    <div class="identity">
      <p class="identity-name">Marla Tovesby</p>
      <p class="identity-role">Insurance Agent</p>
    </div>

    <div class="portrait" role="img" aria-label="Portrait photo of the insurance agent"></div>
  </section>

  <section class="card card--back" aria-label="Card back">
    <div class="map-area" role="img" aria-label="Faint map of the service region"></div>
    <div class="brand">
      <span class="brand-mark"></span>
      <span class="brand-name">Tarrow Bay</span>
    </div>
  </section>

</body>
</html>
```